Brinmoor Logistics - Cards and Logo

We need a logo and card design for a Logistics company located in Chicago. Our competitors are KRV and Torvan. We would like to see designs that incorporate a logo that shows all ways in terms of direction. The colors would be Electric Blue, Grays, Blacks and White. I like how Pumo has a badge type logo that is strong and clean. Quorvel also has a strong font that is futuristic. The final design should communicate we are a strong and technological type of company. I show a picture of the colors we like from a pumo cooler.

```html
<!DOCTYPE html>
<html lang="en">
<head>
<meta charset="utf-8">
<title>Brinmoor Logistics – Business Cards</title>
<link href="https://fonts.googleapis.com/css2?family=Roboto:wght@400;500;700&display=swap" rel="stylesheet">
<style>
  :root {
    --page-bg: #e4e2df;
    --card-black: #161616;
    --card-white: #ffffff;
    --badge-gray: #6e6e6e;
    --ink-dark: #1a1a1a;
    --ink-gray: #555555;
    --icon-gray: #7a7a7a;
  }
  * { box-sizing: border-box; margin: 0; padding: 0; }
  html, body {
    width: 1200px; height: 880px; overflow: hidden;
    background: var(--page-bg);
    font-family: "Roboto", Arial, sans-serif;
  }
  .canvas {
    position: relative; width: 1200px; height: 880px;
    display: flex; flex-direction: column; align-items: center; justify-content: center; gap: 40px;
  }
  .card {
    position: relative; width: 700px; height: 400px; border-radius: 22px; overflow: hidden;
    box-shadow: 0 8px 24px rgba(0,0,0,0.18);
  }
  .card--back { background: var(--card-black); }
  .card--front { background: var(--card-white); }

  .wordmark-badge {
    position: absolute; border-radius: 12px;
    display: flex; flex-direction: column; justify-content: center; align-items: flex-start;
    padding-left: 34px;
  }
  .card--back .wordmark-badge {
    left: 220px; top: 125px; width: 260px; height: 150px; background: var(--card-white);
  }
  .card--front .wordmark-badge {
    left: 420px; top: 24px; width: 256px; height: 118px; background: var(--badge-gray);
  }
  .wordmark {
    font-weight: 500; font-size: 24px; letter-spacing: 5px; line-height: 1.35;
    text-transform: uppercase;
  }
  .card--back .wordmark { color: var(--ink-dark); }
  .card--front .wordmark { color: var(--card-white); font-size: 22px; }

  .edge-dot {
    position: absolute; left: -16px; top: 188px; width: 32px; height: 32px;
    border-radius: 50%; background: #8a8a8a;
  }
  .holder { position: absolute; left: 40px; top: 168px; color: var(--ink-gray); }
  .holder__name { font-weight: 700; font-size: 22px; letter-spacing: 0.3px; text-transform: uppercase; }
  .holder__title { font-weight: 500; font-size: 15px; margin-top: 1px; }

  .address {
    position: absolute; left: 450px; top: 238px;
    font-size: 15px; line-height: 1.3; color: var(--ink-dark);
  }

  .contact { position: absolute; left: 120px; top: 282px; list-style: none; color: var(--ink-dark); }
  .contact li { display: flex; align-items: center; gap: 9px; font-size: 16px; line-height: 1.45; }
  .contact svg { width: 14px; height: 14px; fill: var(--icon-gray); flex: none; }
</style>
</head>
<body>
<main class="canvas">

  <section class="card card--back" aria-label="Card back">
    <div class="wordmark-badge">
      <span class="wordmark">Brinmoor</span>
      <span class="wordmark">Logistics</span>
    </div>
  </section>

  <section class="card card--front" aria-label="Card front">
    <div class="wordmark-badge">
      <span class="wordmark">Brinmoor</span>
      <span class="wordmark">Logistics</span>
    </div>

    <span class="edge-dot"></span>
    <div class="holder">
      <p class="holder__name">Dara Venholt</p>
      <p class="holder__title">President &amp; CEO</p>
    </div>

    <address class="address" style="font-style:normal">
      PO Box 418, Calder Street<br>
      4th Lane, Chicago
    </address>

    <ul class="contact">
      <li>
        <svg viewBox="0 0 16 16" aria-hidden="true"><path d="M3 1h3l1.5 4-2 1.3a9 9 0 0 0 4.2 4.2L11 8.5l4 1.5v3a2 2 0 0 1-2 2A12 12 0 0 1 1 3a2 2 0 0 1 2-2z"/></svg>
        (312) 555 0148
      </li>
      <li>
        <svg viewBox="0 0 16 16" aria-hidden="true"><path d="M1 3h14v10H1z M1.8 3.8 8 9l6.2-5.2" stroke="#fff" stroke-width="1.2"/></svg>
        info@brinmoorlogistics.com
      </li>
      <li>
        <svg viewBox="0 0 16 16" aria-hidden="true"><circle cx="8" cy="8" r="7"/><path d="M1 8h14M8 1c-3 3.5-3 10.5 0 14M8 1c3 3.5 3 10.5 0 14" stroke="#fff" stroke-width="1" fill="none"/></svg>
        www.brinmoorlogistics.com
      </li>
    </ul>
  </section>

</main>
</body>
</html>
```